Dermatology Clinic / Pediatric Clinic / Allergy Clinic

Its a school project so just make up all the information on the flyer.
i need "3 DIFFERENT FLYERS. All 8x12. Can be edited through Microsoft word.
DUE DATE: FRIDAY JUNE 10, 2016 NOT JUNE 22, 2016
First Name of the Project is: Dermatology Clinic,
Second Name of the Project is: Pediatric Clinic,
Last Name of the Project is: Allergy Clinic.
My professors instruction: A prospective client should be able to see your ad and know everything about the specialist and why they might need one. Be sure to utilize colors and pictures.
has accurate information on each flyers. Good knowledge of subject and presentation package well done.
flyer to advertise and promote service AND INFORMATION ON MY CHOSEN PROJECTS to help people gain more knowledge on each specialties.
ON THE FLYERS IT INCLUDE:
1) What services are offered
2) specialties of the clinic
3) Name of the doctor: Corinne Mae Delacruz
4) Address: Address: 415 Birchmere Rd. E. Suite 210, Toronto, ON M4K 2P7
5) Phone:(416) 555-0187
6) Clinic Hours:
(By appointment only)
Monday to Thursday: 8:30am – 3:30pm
Friday: 9:00am – 3:30pm
Saturday & Sunday: Close
and any other necessary information.
Updates
Target Market(s)
Deadline is on July 10, 2016
I dunno how to update the date. :( but it will be soon. July 10 Friday
Visual reminder for professionals working who can generate referrals. Friends and family who would like to purchase a gift certificate for friend/family member.
Pls help. Thank you
Industry/Entity Type
School
Requirements
Must have
- On the flyer it includes.
- 1) What services are offered
- 2) specialties of the clinic
- 3) Name of the doctor: Corinne Mae Delacruz
- 4) Address: Address: 415 Birchmere Rd. E. Suite 210, Toronto, ON M4K 2P7
- 5) Phone:(416) 555-0187
- and any other necessary information.
Nice to have
- made and can open and edit on Microsoft Word

```html
<!DOCTYPE html>
<html lang="en">
<head>
<meta charset="utf-8">
<title>Lumena Dermatology Flyer</title>
<link rel="stylesheet" href="https://fonts.googleapis.com/css2?family=Roboto+Condensed:wght@300;400&family=Arimo:wght@400;700&display=swap">
<style>
  :root {
    --mauve: #9b6b6e;
    --mauve-dark: #7c4f53;
    --panel-pink: #f5dde0;
    --brand-pink: #fbeff1;
    --ink: #111111;
    --text: #333333;
    --muted: #555555;
    --rule: #cfcfcf;
    --white: #ffffff;
    --placeholder: #d9d9d9;
  }
  html, body {
    margin: 0;
    padding: 0;
    overflow: hidden;
    background: var(--white);
  }
  .flyer {
    position: relative;
    width: 800px;
    height: 1200px;
    overflow: hidden;
    background: var(--white);
    font-family: "Arimo", Arial, sans-serif;
  }
  .hero {
    position: absolute;
    left: 0; top: 0;
    width: 800px; height: 623px;
    background:
      radial-gradient(ellipse 240px 300px at 100px 340px, rgba(246,230,232,0.95), rgba(246,230,232,0) 72%),
      radial-gradient(ellipse 250px 320px at 470px 250px, #e6c9bb 0%, #cfab9a 45%, rgba(90,60,55,0) 80%),
      linear-gradient(90deg, #d9c3c0 0%, #6b4d47 32%, #3e2a26 55%, #4a332f 75%, #8c6f69 100%);
  }
  .hero-headline {
    position: absolute;
    left: 46px; top: 296px;
    margin: 0;
    font-family: "Roboto Condensed", "Arial Narrow", sans-serif;
    font-weight: 300;
    font-size: 58px;
    line-height: 73px;
    color: var(--mauve);
  }
  .hero-web {
    position: absolute;
    right: 24px; top: 578px;
    font-size: 20px;
    color: var(--white);
  }
  .service-photo {
    position: absolute;
    top: 623px;
    height: 124px;
  }
  .service-photo--treatment {
    left: 0; width: 271px;
    background: linear-gradient(135deg, #e9e4e2 0%, #d8c0b6 55%, #b89a90 100%);
  }
  .service-photo--mole {
    left: 274px; width: 273px;
    background: linear-gradient(135deg, #f1efee 0%, #d4ab92 50%, #3a3334 100%);
  }
  .service-label {
    position: absolute;
    left: 8px; top: 3px;
    font-size: 13px;
    font-weight: 700;
    color: var(--ink);
    background: rgba(255,255,255,0.7);
    padding: 0 4px;
  }
  .expert-panel {
    position: absolute;
    left: 551px; top: 623px;
    width: 249px; height: 384px;
    background: var(--panel-pink);
    text-align: center;
  }
  .expert-title {
    margin: 44px 0 0;
    font-size: 16px;
    font-weight: 400;
    color: #444;
  }
  .expert-name {
    margin: 3px 0 0;
    font-size: 12px;
    font-weight: 700;
    color: #222;
  }
  .expert-portrait {
    position: absolute;
    left: 56px; top: 80px;
    width: 128px; height: 128px;
    background: var(--placeholder);
    border: 4px solid var(--white);
  }
  .brand-block {
    position: absolute;
    left: 551px; top: 1009px;
    width: 249px; height: 164px;
    background: var(--brand-pink);
  }
  .brand-name {
    position: absolute;
    left: 26px; top: 22px;
    margin: 0;
    font-weight: 400;
    color: var(--mauve-dark);
    line-height: 1;
  }
  .brand-name-main { display: block; font-size: 43px; letter-spacing: 2px; }
  .brand-name-sub { display: block; font-size: 27px; margin-top: 4px; }
  .brand-tagline {
    position: absolute;
    left: 27px; top: 110px;
    font-size: 14px;
    color: var(--muted);
  }
  .brand-address {
    position: absolute;
    left: 26px; top: 134px;
    display: flex;
    gap: 6px;
    font-size: 11px;
    line-height: 14px;
    color: var(--muted);
  }
  .brand-address svg { flex: none; margin-top: 2px; }
  .clinic-info {
    position: absolute;
    left: 44px; top: 774px;
    width: 480px;
    display: grid;
    grid-template-columns: 1fr 1fr;
    column-gap: 28px;
    row-gap: 22px;
    color: var(--text);
  }
  .info-block h3 {
    margin: 0 0 8px;
    font-size: 15px;
    font-weight: 700;
    letter-spacing: 1px;
    text-transform: uppercase;
    color: var(--mauve-dark);
    border-bottom: 2px solid var(--panel-pink);
    padding-bottom: 4px;
  }
  .info-block ul {
    margin: 0;
    padding: 0 0 0 16px;
    font-size: 13px;
    line-height: 20px;
  }
  .info-block--hours { grid-column: 1 / span 2; }
  .hours-note {
    margin: 0 0 4px;
    font-size: 12px;
    font-style: normal;
    color: var(--muted);
  }
  .hours-table {
    border-collapse: collapse;
    font-size: 13px;
    line-height: 20px;
  }
  .hours-table td { padding: 0 24px 0 0; }
  .hours-table td:first-child { font-weight: 700; color: var(--mauve-dark); }
  .cta {
    position: absolute;
    left: 44px; top: 1138px;
    margin: 0;
    font-size: 22px;
    font-weight: 700;
    color: var(--mauve);
  }
  .cta-phone {
    margin-left: 14px;
    font-size: 25px;
    color: var(--ink);
  }
  .footer-rule {
    position: absolute;
    left: 0; top: 1173px;
    width: 800px; height: 1px;
    background: var(--rule);
  }
</style>
</head>
<body>
<main class="flyer">
  <section class="hero" role="img" aria-label="Portrait photo of a woman with long dark hair and clear skin behind soft pink blossoms"></section>
  <h1 class="hero-headline">Enjoy your<br>healthy<br>beautiful<br>skin</h1>
  <div class="hero-web">www.lumenaskin.ca</div>

  <div class="service-photo service-photo--treatment" role="img" aria-label="Photo of a patient receiving a facial skin treatment">
    <span class="service-label">Comprehensive Treatment</span>
  </div>
  <div class="service-photo service-photo--mole" role="img" aria-label="Photo of a doctor examining a mole on a patient's shoulder with a dermatoscope">
    <span class="service-label">Mole Removal</span>
  </div>

  <section class="clinic-info">
    <div class="info-block">
      <h3>Services Offered</h3>
      <ul>
        <li>Full-body skin checks</li>
        <li>Mole &amp; cyst removal</li>
        <li>Acne &amp; scar treatment</li>
        <li>Laser &amp; cosmetic care</li>
      </ul>
    </div>
    <div class="info-block">
      <h3>Our Specialties</h3>
      <ul>
        <li>Eczema &amp; psoriasis</li>
        <li>Skin cancer screening</li>
        <li>Rosacea &amp; allergies</li>
        <li>Hair &amp; nail disorders</li>
      </ul>
    </div>
    <div class="info-block info-block--hours">
      <h3>Clinic Hours</h3>
      <p class="hours-note">By appointment only</p>
      <table class="hours-table">
        <tr><td>Monday to Thursday</td><td>8:30am – 3:30pm</td></tr>
        <tr><td>Friday</td><td>9:00am – 3:30pm</td></tr>
        <tr><td>Saturday &amp; Sunday</td><td>Closed</td></tr>
      </table>
    </div>
  </section>

  <aside class="expert-panel">
    <h2 class="expert-title">Our Dermatology Expert</h2>
    <p class="expert-name">Dr Corinne Mae Delacruz</p>
    <div class="expert-portrait" role="img" aria-label="Space for the doctor's portrait photo"></div>
  </aside>

  <div class="brand-block">
    <h2 class="brand-name">
      <span class="brand-name-main">LUMENA</span>
      <span class="brand-name-sub">DERMATOLOGY</span>
    </h2>
    <div class="brand-tagline">Medical &amp; Cosmetic Services</div>
    <div class="brand-address">
      <svg width="10" height="14" viewBox="0 0 10 14" aria-hidden="true">
        <path d="M5 0C2.2 0 0 2.2 0 5c0 3.6 5 9 5 9s5-5.4 5-9c0-2.8-2.2-5-5-5zm0 7a2 2 0 1 1 0-4 2 2 0 0 1 0 4z" fill="#555"/>
      </svg>
      <span>415 Birchmere Rd. E. Suite 210,<br>Toronto, ON M4K 2P7</span>
    </div>
  </div>

  <p class="cta">Make appointment today: <span class="cta-phone">(416) 555-0187</span></p>
  <div class="footer-rule"></div>
</main>
</body>
</html>
```